Halden & Pruitt Periodontics and Implant Solutions Business Card

We are a specialty dental practice- implants and periodontal surgery. We have just re-designed our logo and are building a new office and would like to re-design our business card. We are looking for something professional with a creative and artsy twist- something to stand out among the rest! Happy Designing!

I have uploaded all versions of our new logo and our current business card. We have 3 locations and 2 doctors.

Target Market(s)

55+

Industry/Entity Type

Dental

Contact Information for Business Card

Needs Names, logo, locations- professional and artsy!

Colors
0555a3
0592cd
34a7d7
3277b5
85cae6
85acd3
cee9f5
ecf7fb

Requirements
Must have
• our names:
• Thomas E. Halden D.M.D.
• Celia M. Pruitt D.M.D.
• Diplomate of the National Council of Gum Surgery
• Address locations:
• 462 W. Larkspur Avenue Suite 210B Plantation, FL 33871
• Tel: 954-318-2264 Fax: 954-318-2291
• 5127 Harlow Lane #C-4 Boca Raton, FL 33609
• Tel: 561-627-1958 Fax: 561-703-2816
• 274 Northwest 9th Street #412 Miami FL 33987
• Tel: 786-429-6153 Fax: 786-429-6170
Nice to have
• unique look
Should not have
• doesn't need QR like our current card has.

```html
<!DOCTYPE html>
<html lang="en">
<head>
<meta charset="utf-8">
<title>Halden &amp; Pruitt Business Card</title>
<link href="https://fonts.googleapis.com/css2?family=Montserrat:wght@400;600;700&family=Roboto+Condensed:wght@400&display=swap" rel="stylesheet">
<style>
  :root {
    --navy: #283470;
    --bright-blue: #0a7cc1;
    --silver: #cfd2d6;
    --paper: #f3f4f4;
    --backdrop: #1d1e20;
    --ink: #2b2b2b;
    --label-blue: #0a6fb5;
    --divider: #b9bcc0;
    --white: #ffffff;
  }
  * { margin: 0; padding: 0; box-sizing: border-box; }
  html, body {
    width: 1200px; height: 1001px; overflow: hidden;
    background: var(--backdrop);
  }
  .card {
    position: absolute; left: 306px;
    width: 587px; height: 328px;
    border-radius: 14px; overflow: hidden;
    background: var(--paper);
  }
  .card--front { top: 134px; }
  .card--back { top: 540px; background: var(--navy); }
  .card__waves { position: absolute; inset: 0; }

  .brand {
    position: absolute; display: flex; align-items: center; gap: 12px;
  }
  .brand__mark {
    width: 86px; height: 86px; border-radius: 50%;
    border: 4px solid currentColor; flex: none;
  }
  .brand__name {
    font-family: "Montserrat", sans-serif; font-weight: 600;
    line-height: 1.05;
  }
  .brand__title { display: block; font-size: 26px; letter-spacing: -0.3px; }
  .brand__tagline { display: block; font-size: 11.5px; letter-spacing: 0.1px; }
  .card--front .brand { left: 50px; top: 55px; color: var(--navy); }
  .card--back .brand { left: 48px; top: 50px; color: var(--white); }

  .credential {
    position: absolute; left: 49px; top: 252px;
    font-family: "Montserrat", sans-serif; font-weight: 400;
    font-size: 13.5px; line-height: 18px; color: var(--white);
  }
  .doctors {
    position: absolute; right: 49px; top: 240px; text-align: right;
    font-family: "Montserrat", sans-serif; color: var(--white);
    font-size: 18.5px; line-height: 29px;
  }
  .doctors__name { font-weight: 700; }
  .doctors__degree { font-weight: 400; }

  .locations {
    position: absolute; left: 0; top: 232px; width: 100%;
    font-family: "Roboto Condensed", sans-serif; font-size: 13.3px;
    line-height: 16.4px; color: var(--ink);
  }
  .location { position: absolute; top: 0; white-space: nowrap; }
  .location:nth-child(1) { left: 30px; }
  .location:nth-child(2) { left: 245px; }
  .location:nth-child(3) { left: 419px; }
  .location__label { color: var(--label-blue); }
  .divider {
    position: absolute; top: 4px; width: 1px; height: 58px;
    background: var(--divider);
  }
  .divider--one { left: 219px; }
  .divider--two { left: 393px; }
</style>
</head>
<body>

<section class="card card--front">
  <svg class="card__waves" viewBox="0 0 587 328" width="587" height="328" aria-hidden="true">
    <path d="M0 178 C140 226 260 170 380 168 C470 166 540 175 587 184 L587 200 C500 178 300 190 0 236 Z" fill="var(--bright-blue)"/>
    <path d="M0 210 C150 236 280 196 400 184 C480 176 540 186 587 200 L587 212 C500 190 300 200 0 236 Z" fill="var(--silver)"/>
    <path d="M0 230 C160 232 290 190 420 180 C500 174 550 186 587 196 L587 328 L0 328 Z" fill="var(--navy)"/>
  </svg>
  <div class="brand">
    <span class="brand__mark"></span>
    <span class="brand__name">
      <span class="brand__title">HALDEN &amp; PRUITT</span>
      <span class="brand__tagline">Periodontics and Implant Solutions</span>
    </span>
  </div>
  <p class="credential">Diplomate of the National<br>Council of Gum Surgery</p>
  <p class="doctors">
    <span class="doctors__name">THOMAS E. HALDEN</span> <span class="doctors__degree">D.M.D.</span><br>
    <span class="doctors__name">CELIA M. PRUITT</span> <span class="doctors__degree">D.M.D.</span>
  </p>
</section>

<section class="card card--back">
  <svg class="card__waves" viewBox="0 0 587 328" width="587" height="328" aria-hidden="true">
    <path d="M0 176 C140 214 280 190 420 158 C500 142 550 140 587 142 L587 328 L0 328 Z" fill="var(--silver)"/>
    <path d="M0 168 C150 200 290 176 420 156 C500 146 550 150 587 156 L587 186 C520 170 440 176 360 190 C240 212 120 222 0 196 Z" fill="var(--bright-blue)"/>
    <path d="M0 194 C120 218 240 214 360 192 C440 178 520 172 587 186 L587 328 L0 328 Z" fill="var(--paper)"/>
    <path d="M0 0 L587 0 L587 140 C540 138 490 146 420 160 C300 186 160 206 0 166 Z" fill="var(--navy)"/>
  </svg>
  <div class="brand">
    <span class="brand__mark"></span>
    <span class="brand__name">
      <span class="brand__title">HALDEN &amp; PRUITT</span>
      <span class="brand__tagline">Periodontics and Implant Solutions</span>
    </span>
  </div>
  <div class="locations">
    <address class="location" style="font-style:normal">
      462 W. Larkspur Avenue<br>
      Suite 210B Plantation, FL 33871<br>
      <span class="location__label">Tel:</span> 954-318-2264<br>
      <span class="location__label">Fax:</span> 954-318-2291
    </address>
    <address class="location" style="font-style:normal">
      5127 Harlow Lane #C-4<br>
      Boca Raton, FL 33609<br>
      <span class="location__label">Tel:</span> 561-627-1958<br>
      <span class="location__label">Fax:</span> 561-703-2816
    </address>
    <address class="location" style="font-style:normal">
      274 Northwest 9th Street<br>
      #412 Miami FL 33987<br>
      <span class="location__label">Tel:</span> 786-429-6153<br>
      <span class="location__label">Fax:</span> 786-429-6170
    </address>
    <span class="divider divider--one"></span>
    <span class="divider divider--two"></span>
  </div>
</section>

</body>
</html>
```